NOTE: I PROVIDED THE INCORRECT LOGO AND ONLY A HANDFUL OF PEOPLE NOTICED THAT IT WAS NOT THE ONE I DESCRIBED. THE LOGO I HAVE NOW ATTACHED MATCHES MY WEBSITE AND THE COLORS ON THE WEBSITE SHOULD BE USED FOR THE CARD.

PLEASE READ THE BUSINESS CARD DETAILS AND PROJECT MUST HAVES CAREFULLY.

I am looking for a business card that is powerful, a bit edgy, and although I work in the corporate world, not too formal. I would like to see designs that use the colors on my website www.brightmoorlane.com. I don't want the card to look washed out so please use shades of those colors that make them "pop". The "vibe" of the card needs to show substance and confidence while also reflecting that we're not your usual consultants.

The focus of my work is turning "people problems" into profits. Those problems could be poor service, an unstable workforce, untrained leaders, or managing change. We are an aggressive, results-focused team of performance improvement professionals who refuse to believe "things can't be done". For us, failure is not an option. Our logo reflects a target from the view of the site on a gun.

In addition to the contact information provided on the sample business card (do not include "turning people problems into profits"), I would like to include this statement (probably on the back):
I equip results-oriented business leaders to turn their people problems into profits in six months or less.

PLEASE NOTE THAT MY WEBSITE IS UNDER REVISION TO TONE DOWN THE MILITARY THEME, ALTHOUGH THE WARRIOR ENERGY AND FOCUS ON RESULTS REMAINS.

Target Market(s)

My clients are Mid and senior-level managers. I don't target any particular industry.

Industry/Entity Type

Consulting

Contact Information for Business Card

In addition to the contact information provided on the sample business card (DO NOT INCLUDE "turning people problems into profits"), I would like to include this statement (probably on the back):

I don't care whether the card is landscape or portrait view.

Font styles to use
Sans Serif

Requirements
Must have
• 1. be easy to read, no 6-8 point fonts!
• 2. a "vibe" that captures the eye without being too chaotic or busy
• 3. bold color, not washed out or boring - a good blend with the colors currently on my website (black, red, white, army green) but you don't need to use all of them.
• 4. all the contact information I have provided
• 5. a good blend with the colors currently on my website
• 6. Must have this quote on the back of the card: I equip results-oriented business leaders to turn their people problems into profits in six months or less.
Nice to have
• In looking at the sample images I provided for ideas, you can see that I like the way a card carries over from one side to the next.
• It would be great to find some aspect/quality/feature that I haven't seen before
Should not have
• 1. NO use of ALL CAPS
• 2. fonts that I would have to seek out and purchase (you should provide files for font if using something not standard)

```html
<!DOCTYPE html>
<html lang="en">
<head>
<meta charset="utf-8">
<title>Brightmoor Lane Inc — Business Card</title>
<link href="https://fonts.googleapis.com/css2?family=Questrial&display=swap" rel="stylesheet">
<style>
  :root {
    --backdrop: #4a4a4a;
    --card: #161616;
    --card-edge: #262626;
    --army-green: #8aa43a;
    --signal-red: #e0322b;
    --ink-white: #f2f2f2;
    --ink-soft: #d4d4d4;
    --rule: #3a3a3a;
  }
  * { box-sizing: border-box; margin: 0; padding: 0; }
  html, body {
    width: 1200px; height: 752px; overflow: hidden;
    background: var(--backdrop);
    font-family: "Questrial", "Century Gothic", sans-serif;
  }
  .canvas {
    position: relative; width: 1200px; height: 752px;
    display: flex; align-items: center; justify-content: center; gap: 60px;
  }
  .card {
    position: relative; width: 520px; height: 297px;
    background: var(--card);
    border: 1px solid var(--card-edge);
    overflow: hidden;
  }

  /* Contact side */
  .brand-mark {
    position: absolute; left: 40px; top: 44px;
    display: flex; align-items: center; gap: 10px;
    color: var(--army-green); font-size: 20px;
  }
  .brand-mark .square { width: 14px; height: 14px; background: var(--signal-red); }
  .identity {
    position: absolute; right: 40px; top: 96px; text-align: right;
    width: 260px; padding-bottom: 8px;
    border-bottom: 1px solid var(--rule);
  }
  .identity .name { color: var(--signal-red); font-size: 19px; }
  .identity .title { color: var(--army-green); font-size: 15px; margin-top: 2px; }
  .contacts {
    position: absolute; right: 40px; top: 160px;
    list-style: none;
  }
  .contacts li {
    display: flex; align-items: center; justify-content: flex-end; gap: 12px;
    color: var(--ink-white); font-size: 14px; height: 26px;
  }
  .contacts .icon {
    width: 16px; height: 16px; border-radius: 50%;
    background: var(--army-green);
    display: flex; align-items: center; justify-content: center;
  }
  .contacts .icon svg { width: 10px; height: 10px; }

  /* Brand side */
  .accent-bar { position: absolute; height: 8px; background: var(--army-green); }
  .accent-bar.top { top: 0; right: 0; width: 215px; }
  .accent-bar.bottom { bottom: 0; left: 95px; width: 215px; }
  .wordmark {
    position: absolute; left: 0; right: 0; top: 84px;
    text-align: center;
  }
  .wordmark .company {
    display: inline-flex; align-items: center; gap: 10px;
    color: var(--army-green); font-size: 38px;
  }
  .wordmark .company .square { width: 12px; height: 12px; background: var(--signal-red); }
  .wordmark .statement {
    width: 380px; margin: 18px auto 0;
    color: var(--ink-soft); font-size: 14px; line-height: 1.5;
  }
</style>
</head>
<body>
<main class="canvas">
  <section class="card card-contact" aria-label="Contact side">
    <div class="brand-mark"><span class="square"></span>Brightmoor Lane</div>
    <div class="identity">
      <p class="name">Dana Whitfield</p>
      <p class="title">Chief Performance Strategist</p>
    </div>
    <ul class="contacts">
      <li>555-014-2290
        <span class="icon"><svg viewBox="0 0 10 10"><path d="M2 1l2 2-1 1.2a6 6 0 002.8 2.8L7 6l2 2-1.3 1.3C4.5 9 1 5.5.7 2.3z" fill="#161616"/></svg></span>
      </li>
      <li>555-017-4831
        <span class="icon"><svg viewBox="0 0 10 10"><rect x="2.5" y="0.5" width="5" height="9" rx="1" fill="#161616"/><rect x="3.5" y="1.8" width="3" height="5" fill="#8aa43a"/></svg></span>
      </li>
      <li>danaw@brightmoorlane.com
        <span class="icon"><svg viewBox="0 0 10 10"><rect x="1" y="2.5" width="8" height="5" fill="#161616"/><path d="M1 2.5l4 3 4-3" stroke="#8aa43a" stroke-width=".8" fill="none"/></svg></span>
      </li>
      <li>www.brightmoorlane.com
        <span class="icon"><svg viewBox="0 0 10 10"><circle cx="5" cy="5" r="4" fill="#161616"/><path d="M1 5h8M5 1c-2 2.5-2 5.5 0 8M5 1c2 2.5 2 5.5 0 8" stroke="#8aa43a" stroke-width=".7" fill="none"/></svg></span>
      </li>
    </ul>
  </section>

  <section class="card card-brand" aria-label="Brand side">
    <span class="accent-bar top"></span>
    <div class="wordmark">
      <p class="company">Brightmoor Lane<span class="square"></span></p>
      <p class="statement">I equip results-oriented business leaders to turn their people problems into profits in six months or less.</p>
    </div>
    <span class="accent-bar bottom"></span>
  </section>
</main>
</body>
</html>
```